Webdesign für Gemeinschaftspraxis (13820)
Zielgruppe
Die Website ist für eine fachärztliche Gemeinschaftspraxis, die sich aus Internisten, Betriebsmedizinern, Präventionsärzten, Kardiologen, Allgemeinmedizinern und Phlebologen zusammensetzt.
Die Zielgruppe sind bestehende Patienten sowie potentielle Patienten.
Die Website soll informativ sein.
Aufgabenstellung
Die Website soll in schlichten Farben gehalten sein, die zum Logo und zu den Fotos passen.
Die Website soll als kurzer, informativer Auftritt dienen
Die gelieferten Fotos sollen verwendet werden.
Es soll eine Onepage-Website werden, die so aufgebaut ist, wie die Website unter dem folgenden Link: https://www.kolbenfeld-portal.de/

```html
<!DOCTYPE html>
<html lang="de">
<head>
<meta charset="utf-8">
<title>Gemeinschaftspraxis Lindenhof</title>
<link rel="stylesheet" href="https://fonts.googleapis.com/css2?family=Montserrat:wght@400;500;600&family=Oswald:wght@400&family=Roboto+Slab:wght@300;400&family=Raleway:wght@300;400&display=swap">
<style>
:root{
  --brown:#9a6648;
  --navy:#25376a;
  --navy-band:#2c3f6e;
  --link:#3f8bc6;
  --text:#333;
  --muted:#666;
  --line:#e3e3e3;
  --paper:#f5f7fb;
  --white:#fff;
}
*{box-sizing:border-box;margin:0;padding:0}
html,body{width:1200px;height:2724px;overflow:hidden;background:var(--white);font-family:"Raleway",sans-serif;color:var(--text)}
.page{position:relative;width:1200px;height:2724px}
.site-header{position:absolute;top:0;left:0;width:1200px;height:157px;border-bottom:2px solid var(--brown)}
.brand{position:absolute;top:22px;left:0;width:1200px;text-align:center}
.brand-name{font-family:"Montserrat",sans-serif;font-weight:600;font-size:22px;color:var(--navy);letter-spacing:1px}
.brand-sub{font-family:"Montserrat",sans-serif;font-weight:600;font-size:22px;color:var(--navy);display:block;margin-top:4px;letter-spacing:1px}
.main-nav{position:absolute;top:120px;left:0;width:1200px;text-align:center;font-family:"Oswald",sans-serif;font-size:14px;color:var(--brown)}
.main-nav span{margin:0 10px;text-transform:uppercase}
.search-btn{position:absolute;top:113px;left:1088px;width:41px;height:34px;background:#666}
.hero{position:absolute;top:157px;left:0;width:1200px;height:569px;background:linear-gradient(180deg,#c9bba6 0%,#a88d70 45%,#6d6259 75%,#b8b4ae 100%)}
.hero-title{position:absolute;top:148px;left:0;width:1200px;text-align:center;font-family:"Montserrat",sans-serif;font-size:40px;line-height:42px;color:var(--white)}
.hero-text{position:absolute;top:263px;left:375px;width:450px;text-align:center;font-family:"Roboto Slab",serif;font-size:13px;line-height:19px;color:var(--white)}
.dots{position:absolute;top:518px;left:575px}
.dots i{display:inline-block;width:11px;height:11px;border:2px solid #555;margin-right:7px;background:rgba(255,255,255,.6)}
.section-title{position:absolute;left:0;width:1200px;text-align:center;font-family:"Montserrat",sans-serif;font-size:27px;color:var(--brown)}
.treatments{position:absolute;top:866px;left:187px;width:825px;list-style:none}
.treatments li{height:51px;border-bottom:1px solid var(--line);padding:7px 0 0 27px;font-family:"Roboto Slab",serif;font-weight:300;font-size:17px;color:var(--link)}
.section-sub{position:absolute;left:0;width:1200px;text-align:center;font-family:"Montserrat",sans-serif;font-size:12.5px}
.member{position:absolute;top:1418px;width:140px;text-align:center}
.avatar{width:124px;height:124px;border-radius:50%;margin:0 auto}
.member-name{margin-top:42px;font-family:"Montserrat",sans-serif;font-weight:600;font-size:12px;color:var(--text)}
.member-rule{width:78px;height:2px;margin:6px auto 10px}
.member-role{font-family:"Montserrat",sans-serif;font-size:10px;color:var(--muted)}
.hours{position:absolute;top:1748px;left:0;width:1200px;height:628px;background:linear-gradient(180deg,#2f4272,#273a69)}
.hours .section-title{color:var(--white)}
.hours .section-sub{color:#d0d6e4;font-family:"Raleway",sans-serif}
.info-box{position:absolute;left:180px;width:381px;background:rgba(255,255,255,.12);color:var(--white)}
.info-box svg{position:absolute;left:25px}
.info-box h3{position:absolute;left:71px;top:10px;font-family:"Montserrat",sans-serif;font-weight:500;font-size:22px}
.info-box p{position:absolute;left:71px;font-size:12px;line-height:16px;color:#d8deea}
.map{position:absolute;top:1948px;left:592px;width:428px;height:328px;background:linear-gradient(135deg,#e9e3d6,#dfe6d2 50%,#e8ddd2)}
.cta{position:absolute;top:2376px;left:0;width:1200px;height:149px;background:var(--paper);border-bottom:1px solid var(--line)}
.cta-text{position:absolute;top:106px;left:180px;font-family:"Raleway",sans-serif;font-weight:300;font-size:21px;color:#555}
.btn{position:absolute;top:104px;width:191px;height:28px;font-family:"Montserrat",sans-serif;font-weight:600;font-size:11px;text-align:center;line-height:28px}
.btn-call{left:614px;background:var(--brown);color:var(--white)}
.btn-mail{left:820px;background:var(--white);color:var(--brown);border:1px solid #eee}
.site-footer{position:absolute;top:2526px;left:0;width:1200px;height:198px;background:var(--paper)}
.contact{position:absolute;top:62px;left:180px;list-style:none;font-size:12px;color:#444}
.contact li{height:26px;display:flex;align-items:center}
.contact svg{margin-right:12px}
.footer-col{position:absolute;top:30px;text-align:right;font-size:12.5px;line-height:19px;color:#444}
.footer-col h4{font-family:"Montserrat",sans-serif;font-weight:600;font-size:10px;color:#222;margin-bottom:15px}
</style>
</head>
<body>
<div class="page">
  <header class="site-header">
    <div class="brand">
      <span class="brand-name">GEMEINSCHAFTSPRAXIS</span>
      <span class="brand-sub">LINDENHOF</span>
    </div>
    <nav class="main-nav"><span>Startseite</span><span>Behandlungen</span><span>Team</span><span>Öffnungszeiten</span><span>Kontakt</span></nav>
    <div class="search-btn">
      <svg width="41" height="34" viewBox="0 0 41 34"><circle cx="19.5" cy="16" r="4" fill="none" stroke="#fff" stroke-width="1.8"/><line x1="22.5" y1="19" x2="25" y2="21.5" stroke="#fff" stroke-width="2"/></svg>
    </div>
  </header>

  <section class="hero" role="img" aria-label="Foto des Empfangsbereichs der Praxis mit Holztresen und Wartebereich">
    <h1 class="hero-title">Willkommen in unserer<br>Gemeinschaftspraxis</h1>
    <p class="hero-text">Enim ad minim veniam, quis nostrud exercitation ullamco laboris nisi ut aliquip ex ea commodo conse quat. Duis aute irure dolor in reprehenderit in voluptate.</p>
    <div class="dots"><i></i><i></i><i></i></div>
  </section>

  <h2 class="section-title" style="top:789px">WELCHE BEHANDLUNGEN BIETEN WIR AN?</h2>
  <ul class="treatments">
    <li>Gesundheitsvorsorge/Prävention/Gesundheits-Check-up</li>
    <li>Impfungen und Reiseimpfungen</li>
    <li>Männervorsorge</li>
    <li>Diabetes mellitus</li>
    <li>Psychosomatische Grundversorgung</li>
    <li>usw.</li>
  </ul>

  <h2 class="section-title" style="top:1302px">PRAXISTEAM</h2>
  <p class="section-sub" style="top:1344px">Hier können Sie einen kurzen Text über Teambuilding oder ähnliches schreiben.</p>

  <div class="member" style="left:215px"><div class="avatar" role="img" aria-label="Porträtfoto Dr. Harmsen" style="background:linear-gradient(135deg,#2d3f8c,#8a7d98)"></div><div class="member-name">DR. HARMSEN</div><div class="member-rule" style="background:#e0736a"></div><div class="member-role">Disziplin</div></div>
  <div class="member" style="left:425px"><div class="avatar" role="img" aria-label="Porträtfoto Dr. Wolters" style="background:linear-gradient(135deg,#2d3f8c,#8a7d98)"></div><div class="member-name">DR. WOLTERS</div><div class="member-rule" style="background:#5cc3a2"></div><div class="member-role">Disziplin</div></div>
  <div class="member" style="left:635px"><div class="avatar" role="img" aria-label="Porträtfoto Brakemann" style="background:linear-gradient(135deg,#2d3f8c,#8a7d98)"></div><div class="member-name">BRAKEMANN</div><div class="member-rule" style="background:#57a9d9"></div><div class="member-role">Disziplin</div></div>
  <div class="member" style="left:845px"><div class="avatar" role="img" aria-label="Porträtfoto Frau Kessler" style="background:linear-gradient(135deg,#c9b08a,#7a5a42)"></div><div class="member-name">FRAU KESSLER</div><div class="member-rule" style="background:#f0d36a"></div><div class="member-role">Pflege</div></div>

  <section class="hours" role="img" aria-label="Blau getöntes Foto eines Praxisflurs als Hintergrund">
    <h2 class="section-title" style="top:67px">UNSERE ÖFFNUNGSZEITEN</h2>
    <p class="section-sub" style="top:124px">Hier können Sie einen beliebigen Text zur Lokalität oder ähnlichem schreiben.</p>
  </section>
  <div class="info-box" style="top:1948px;height:86px">
    <svg style="top:25px" width="34" height="34" viewBox="0 0 34 34"><circle cx="17" cy="17" r="14" fill="none" stroke="var(--navy)" stroke-width="3.5"/><path d="M17 9v8h-5" fill="none" stroke="var(--navy)" stroke-width="3"/></svg>
    <h3>Öffnungszeiten</h3>
    <p style="top:50px">Hier kommen die Öffnungszeiten</p>
  </div>
  <div class="info-box" style="top:2081px;height:136px">
    <svg style="top:24px" width="30" height="36" viewBox="0 0 30 36"><path d="M15 2a11 11 0 0 0-11 11c0 8 11 21 11 21s11-13 11-21A11 11 0 0 0 15 2z" fill="var(--navy)"/><circle cx="15" cy="13" r="4" fill="#8e9bbf"/></svg>
    <h3>Adresse</h3>
    <p style="top:52px">Ihre Adresse<br>Stadt<br>Deutschland<br>Telefonnummer</p>
  </div>
  <div class="map" role="img" aria-label="Eingebettete Stadtkarte mit Praxisstandort"></div>

  <section class="cta">
    <p class="cta-text">Möchten Sie einen Termin vereinbaren?</p>
    <div class="btn btn-call">ANRUFEN</div>
    <div class="btn btn-mail">E-MAIL SCHREIBEN</div>
  </section>

  <footer class="site-footer">
    <ul class="contact">
      <li><svg width="12" height="12" viewBox="0 0 12 12"><path d="M2 1l2.5 0 1 3-1.5 1c.7 1.4 1.6 2.3 3 3l1-1.5 3 1V11C6 11 1 6 1 2z" fill="#444"/></svg>0049-12345678</li>
      <li><svg width="12" height="12" viewBox="0 0 12 12"><path d="M1 6l10-5-3 10-2-4z" fill="none" stroke="#444"/></svg>praxis@lindenhof-beispiel.de</li>
      <li><svg width="12" height="12" viewBox="0 0 12 12"><rect x="2" y="1" width="8" height="10" fill="none" stroke="#444"/><path d="M4 3h1M7 3h1M4 6h1M7 6h1" stroke="#444"/></svg>Ahornweg 17, Musterstadt</li>
    </ul>
    <div class="footer-col" style="right:465px"><h4>LINKS</h4>Startseite<br>Team<br>Öffnungszeiten<br>Kontakt</div>
    <div class="footer-col" style="right:180px"><h4>WICHTIGES</h4>Datenschutzrichtlinien<br>Impressum</div>
  </footer>
</div>
</body>
</html>
```